Building company requiring web site design

We need a web design for a new company based in Sydney called Harbin Building Co. We build and renovate new and existing homes for consumers. We would like to see design that use the colours red and grey. The final design should communicate innovative building but with old fashion quality, great customer service and attention to detail. I have already had a logo and stationary design completed and would like to use the these colour schemes
Updates

Target Market(s)

Home owners, investors

Industry/Entity Type

Building

Coding

Coded - Design and coding required

Number of Pages Required

5+ page

Requirements
Must have
• Home page, contact page, about us page, gallery page and testimonial page
Nice to have
• Contact form

```html
<!DOCTYPE html>
<html lang="en">
<head>
<meta charset="utf-8">
<title>Harbin Building Co</title>
<link rel="stylesheet" href="https://fonts.googleapis.com/css2?family=Montserrat:wght@400;600;700&display=swap">
<style>
:root{
  --red:#e8174f;
  --ink:#2b2b2b;
  --panel:#2d2f2f;
  --paper:#eef3f6;
  --footer:#2b2e33;
  --footer-bar:#34373c;
  --muted:#8a8f96;
  --white:#ffffff;
}
*{margin:0;padding:0;box-sizing:border-box}
html,body{width:1200px;height:3301px;overflow:hidden}
body{position:relative;font-family:"Montserrat",sans-serif;color:var(--ink);background:var(--paper)}
.abs{position:absolute}
.accent{color:var(--red)}
.site-header{left:0;top:0;width:1200px;height:82px;background:var(--white)}
.brand{left:40px;top:18px;font-size:17px;font-weight:700;color:var(--red);display:flex;align-items:center;gap:8px}
.brand-mark{width:14px;height:14px;background:var(--red)}
.nav a{position:absolute;top:16px;font-size:12px;color:var(--ink);text-decoration:none}
.search{left:1144px;top:50px}
.hero{left:0;top:82px;width:1200px;height:653px;background:linear-gradient(180deg,#6b6f6d 0%,#4a4f4d 55%,#3c3e3d 100%)}
.hero-title{left:0;width:1200px;text-align:center;color:var(--white);font-size:58px;font-weight:400;line-height:1}
.hero-title b{font-weight:700}
.section-title{left:0;width:1200px;text-align:center;font-size:42px;font-weight:400}
.rule{height:1px;background:var(--ink)}
.intro{left:160px;width:880px;top:846px;text-align:center;font-size:24px;line-height:30px}
.panel{background:var(--panel);color:var(--white);font-size:19px;line-height:22px}
.service-name{font-size:50px;font-weight:700;color:var(--red);text-align:center}
.client-name{font-size:22px;font-weight:700;text-align:center;width:300px}
.quote{font-size:28px;line-height:33px}
.quote-mark{font-size:64px;font-weight:700;font-style:normal;line-height:1}
.avatar{width:92px;height:92px;border-radius:50%;background:linear-gradient(180deg,#9aa0a4,#6d7276)}
.see-all{left:529px;top:2227px;width:142px;height:50px;border-radius:25px;background:var(--red);color:var(--white);font-size:25px;text-align:center;line-height:50px}
.map{left:0;top:2531px;width:1200px;height:507px;background:linear-gradient(135deg,#e9e6df 0%,#e4e1da 55%,#a9c4ec 75%,#9dbde9 100%)}
.map-label{left:797px;top:2592px;font-size:38px;color:var(--ink)}
.site-footer{left:0;top:3074px;width:1200px;height:227px;background:var(--footer);color:var(--white)}
.contact-line{left:15px;font-size:15px}
.newsletter{left:420px;top:3120px;width:350px;height:40px;border:1px solid var(--muted);border-radius:20px;color:var(--muted);font-size:13px;font-weight:600;padding:13px 0 0 30px}
.social{width:14px;height:14px;border-radius:50%;background:var(--muted);top:3127px}
.social-active{left:1088px;top:3114px;width:40px;height:40px;border-radius:50%;background:var(--red)}
.footer-bar{left:20px;top:3210px;width:1150px;height:60px;background:var(--footer-bar)}
.footer-link{top:3234px;font-size:14px;font-weight:600;color:var(--muted)}
</style>
</head>
<body>

<header class="abs site-header">
  <div class="abs brand"><span class="brand-mark"></span>Harbin Building Co</div>
  <nav class="nav">
    <a style="left:683px">HOME</a>
    <a style="left:778px">GALLERY</a>
    <a style="left:876px">TESTIMINOL</a>
    <a style="left:989px">ABOUT US</a>
    <a style="left:1099px">CONTACT US</a>
  </nav>
  <svg class="abs search" width="36" height="24" viewBox="0 0 36 24" aria-label="Search">
    <rect x="1" y="1" width="34" height="22" rx="11" fill="none" stroke="var(--ink)" stroke-width="2"/>
    <circle cx="17" cy="11" r="3.5" fill="none" stroke="var(--ink)" stroke-width="1.6"/>
    <path d="M19.5 13.5 L22 16" stroke="var(--ink)" stroke-width="1.6" stroke-linecap="round"/>
  </svg>
</header>

<section class="abs hero" role="img" aria-label="Photograph of a classic car parked in front of a house with a white picket fence"></section>
<h1 class="abs hero-title" style="top:182px">Still living in a <b>house?</b></h1>
<p class="abs hero-title" style="top:268px;font-size:46px">or</p>
<p class="abs hero-title" style="top:333px">Still dreaming about a <b>house?</b></p>
<svg class="abs" style="left:562px;top:585px" width="76" height="76" viewBox="0 0 76 76" aria-label="Scroll down">
  <circle cx="38" cy="38" r="35" fill="none" stroke="#fff" stroke-width="3"/>
  <path d="M22 30 L38 46 L54 30" fill="none" stroke="#fff" stroke-width="3.5" stroke-linecap="round"/>
</svg>

<h2 class="abs section-title" style="top:774px">Who are we ?</h2>
<p class="abs intro"><span class="accent">We</span> are a company that build and renovate new and existing homes for consumers.</p>
<div class="abs rule" style="left:480px;top:979px;width:215px"></div>
<h2 class="abs section-title" style="top:1028px;left:22px"><span class="accent">Our</span> services</h2>

<h3 class="abs service-name" style="left:0;top:1110px;width:516px">Building</h3>
<svg class="abs" style="left:200px;top:1212px" width="116" height="124" viewBox="0 0 116 124" aria-label="Building icon">
  <path d="M42 28 A46 46 0 1 0 92 44" fill="none" stroke="var(--panel)" stroke-width="12"/>
  <path d="M60 70 L86 20" stroke="var(--panel)" stroke-width="12"/>
  <path d="M64 18 L100 4 L98 44 Z" fill="var(--panel)"/>
</svg>
<div class="abs panel" style="left:605px;top:1104px;width:595px;height:296px;padding:44px 20px 0 20px">Lorem ipsum dolor sit amet, consectetur adipiscing elit. Vestibulum nibh elit, auctor cursus turpis in, euismod porta est. In eget erat vel felis porta porta vitae in ante. Donec finibus tincidunt tempus. Donec tincidunt odio ex, non volutpat risus sagittis ut. Vestibulum at nunc eros.</div>

<div class="abs panel" style="left:0;top:1400px;width:605px;height:297px;padding:53px 10px 0 30px;text-align:right">Lorem ipsum dolor sit amet, consectetur adipiscing elit. Vestibulum nibh elit, auctor cursus turpis in, euismod porta est. In eget erat vel felis porta porta vitae in ante. Donec finibus tincidunt tempus. Donec tincidunt odio ex, non volutpat risus sagittis ut. Vestibulum at nunc eros.</div>
<h3 class="abs service-name" style="left:605px;top:1418px;width:640px">Renovating</h3>
<svg class="abs" style="left:846px;top:1520px" width="108" height="108" viewBox="0 0 108 108" aria-label="Renovating icon">
  <path d="M16 48 A38 38 0 0 1 84 28" fill="none" stroke="var(--panel)" stroke-width="13"/>
  <path d="M72 36 L100 38 L98 8 Z" fill="var(--panel)"/>
  <path d="M92 60 A38 38 0 0 1 24 80" fill="none" stroke="var(--panel)" stroke-width="13"/>
  <path d="M36 72 L8 70 L10 100 Z" fill="var(--panel)"/>
</svg>

<div class="abs rule" style="left:400px;top:1809px;width:375px"></div>
<h2 class="abs section-title" style="top:1837px;font-size:36px">what <span class="accent">our</span> customers say...</h2>

<div class="abs avatar" style="left:202px;top:1952px" role="img" aria-label="Client portrait placeholder"></div>
<p class="abs client-name" style="left:104px;top:2056px">Client <span class="accent">Name</span></p>
<i class="abs quote-mark" style="left:58px;top:2110px">&ldquo;</i>
<p class="abs quote" style="left:110px;top:2110px;width:440px">Lorem ipsum dolor sit amet, consectetur adipiscing elit.....</p>

<div class="abs avatar" style="left:834px;top:1952px" role="img" aria-label="Client portrait placeholder"></div>
<p class="abs client-name" style="left:736px;top:2056px">Client <span class="accent">Name</span></p>
<i class="abs quote-mark" style="left:690px;top:2110px">&ldquo;</i>
<p class="abs quote" style="left:742px;top:2110px;width:440px">Lorem ipsum dolor sit amet, consectetur adipiscing elit.....</p>

<div class="abs see-all">See All &gt;</div>

<div class="abs rule" style="left:492px;top:2334px;width:213px"></div>
<h2 class="abs section-title" style="top:2418px;left:4px;font-size:36px"><span class="accent">We</span> are here...</h2>

<section class="abs map" role="img" aria-label="Street map of a harbourside area showing the office location"></section>
<svg class="abs" style="left:734px;top:2586px" width="52" height="70" viewBox="0 0 52 70" aria-label="Location pin">
  <path d="M26 2 C12 2 2 12 2 26 C2 44 26 68 26 68 C26 68 50 44 50 26 C50 12 40 2 26 2 Z" fill="var(--red)"/>
  <circle cx="26" cy="25" r="8" fill="#fff"/>
</svg>
<p class="abs map-label"><span class="accent">Harbin</span> Building Co.</p>

<footer class="abs site-footer"></footer>
<p class="abs contact-line" style="top:3118px;color:#fff">admin@harbinbuildingco.com.au</p>
<p class="abs contact-line" style="top:3148px;color:#fff">0400 555 018</p>
<div class="abs newsletter">Subscribe to our Newsletter</div>
<svg class="abs" style="left:728px;top:3130px" width="24" height="20" viewBox="0 0 24 20" aria-label="Send">
  <path d="M2 2 L22 10 L2 18 L6 10 Z" fill="none" stroke="var(--muted)" stroke-width="2"/>
</svg>
<div class="abs social" style="left:977px" aria-label="Social link"></div>
<div class="abs social" style="left:1017px" aria-label="Social link"></div>
<div class="abs social" style="left:1059px" aria-label="Social link"></div>
<div class="abs social-active" aria-label="Social link"></div>
<div class="abs social" style="left:1141px" aria-label="Social link"></div>
<div class="abs footer-bar"></div>
<p class="abs footer-link" style="left:51px">Privacy Policy</p>
<p class="abs footer-link" style="left:203px">Terms of Use</p>
<p class="abs footer-link" style="left:1024px">Back to top &nbsp;&nbsp;&#8963;</p>

</body>
</html>
```